Quillbrook Builders Business Cards

I want to use the logo and make an unique business card that shows the textured Logo with brick and builings. I want to be able to stand out when I pass out business cards.

```html
<!DOCTYPE html>
<html lang="en">
<head>
<meta charset="UTF-8">
<title>Quillbrook Builders Business Cards</title>
<link rel="stylesheet" href="https://fonts.googleapis.com/css2?family=Montserrat:wght@400;500;700;800&display=swap">
<style>
  :root {
    --bg: #2b2b2b;
    --card: #050505;
    --card-edge: #1a1a1a;
    --accent: #f0521f;
    --icon: #e0332b;
    --text: #f2f2f2;
  }
  * { box-sizing: border-box; margin: 0; padding: 0; }
  html, body { width: 1200px; height: 875px; overflow: hidden; }
  body {
    background: var(--bg);
    font-family: "Montserrat", sans-serif;
    position: relative;
  }
  .card {
    position: absolute;
    width: 560px;
    height: 320px;
    background: var(--card);
    border: 1px solid var(--card-edge);
    border-radius: 18px;
    box-shadow: 0 20px 50px rgba(0,0,0,0.55);
  }
  .card-front { left: 60px; top: 80px; display: flex; align-items: center; justify-content: center; }
  .card-back { left: 580px; top: 475px; }
  .brand-name {
    color: var(--accent);
    font-weight: 800;
    text-transform: uppercase;
    letter-spacing: 1px;
    line-height: 1.05;
    text-align: center;
  }
  .card-front .brand-name { font-size: 40px; }
  .card-back .brand-name {
    position: absolute;
    left: 40px; top: 118px;
    width: 230px;
    font-size: 26px;
  }
  .divider {
    position: absolute;
    left: 300px; top: 60px;
    width: 2px; height: 200px;
    background: var(--accent);
  }
  .details { position: absolute; left: 328px; top: 62px; color: var(--text); }
  .person-name { color: var(--accent); font-weight: 700; font-size: 24px; }
  .person-role { font-size: 13px; font-weight: 500; margin-top: 2px; }
  .address { font-size: 13px; line-height: 1.35; margin-top: 16px; }
  .contacts { list-style: none; margin-top: 16px; font-size: 12.5px; }
  .contacts li { display: flex; align-items: center; gap: 9px; margin-bottom: 6px; }
  .contacts svg { width: 13px; height: 13px; flex: none; }
</style>
</head>
<body>
  <section class="card card-front">
    <p class="brand-name">Quillbrook<br>Builders</p>
  </section>

  <section class="card card-back">
    <p class="brand-name">Quillbrook<br>Builders</p>
    <div class="divider"></div>
    <div class="details">
      <p class="person-name">Daniel Reyes</p>
      <p class="person-role">Managing Director</p>
      <p class="address">48 Harbor Lane,<br>Fairview, USA</p>
      <ul class="contacts">
        <li>
          <svg viewBox="0 0 16 16" aria-hidden="true"><path fill="var(--icon)" d="M3.5 1.5l2.5 0 1 3.5-1.8 1.2c.8 1.8 2.1 3.1 3.9 3.9L10.3 8.3l3.5 1v2.5c0 1-.8 1.7-1.8 1.7C6.6 13.5 2 8.9 1.8 3.3 1.8 2.3 2.5 1.5 3.5 1.5z"/></svg>
          (08) 4431 2208
        </li>
        <li>
          <svg viewBox="0 0 16 16" aria-hidden="true"><rect x="1" y="3" width="14" height="10" rx="1" fill="var(--icon)"/><path d="M1.5 3.8L8 9l6.5-5.2" stroke="#050505" stroke-width="1.4" fill="none"/></svg>
          hello@quillbrookbuilders.com
        </li>
        <li>
          <svg viewBox="0 0 16 16" aria-hidden="true"><circle cx="8" cy="8" r="6.5" fill="none" stroke="var(--icon)" stroke-width="1.6"/><ellipse cx="8" cy="8" rx="2.6" ry="6.5" fill="none" stroke="var(--icon)" stroke-width="1.3"/><line x1="1.5" y1="8" x2="14.5" y2="8" stroke="var(--icon)" stroke-width="1.3"/></svg>
          www.quillbrookbuilders.com
        </li>
      </ul>
    </div>
  </section>
</body>
</html>
```